Maple Lantern Business Card

Design of business cards

Target Market(s)

We are aiming as small business owners who need anything from basic business structures, website plans, business processes and quality assurance.

Industry/Entity Type

Business

Colors

Designer to choose colors to be used in the design.

Requirements
Nice to have
• I would prefer one side of the card to use the green from the logo. Prefer to have the same font as the logo.

```html
<!DOCTYPE html>
<html lang="en">
<head>
<meta charset="utf-8">
<title>Maple Lantern Business Card</title>
<link rel="stylesheet" href="https://fonts.googleapis.com/css2?family=Cinzel:wght@400&family=Exo+2:wght@400;600&display=swap">
<style>
  :root {
    --page-bg: #e6e6e4;
    --card-bg: #ffffff;
    --brand-green: #9ccb3b;
    --ink-dark: #262626;
    --ink-mid: #4a4a4a;
    --rule-grey: #a6a6a6;
  }
  * { box-sizing: border-box; margin: 0; padding: 0; }
  html, body {
    width: 1200px;
    height: 1057px;
    overflow: hidden;
    background: var(--page-bg);
  }
  .canvas {
    position: relative;
    width: 1200px;
    height: 1057px;
  }
  .card {
    position: absolute;
    left: 330px;
    top: 56px;
    width: 540px;
    height: 945px;
    background: var(--card-bg);
    box-shadow: 0 6px 24px rgba(0,0,0,0.12);
  }
  .brand {
    position: absolute;
    left: 70px;
    top: 90px;
    display: flex;
    align-items: center;
    gap: 22px;
  }
  .brand-mark {
    width: 58px;
    height: 58px;
    border-radius: 50%;
    background: var(--brand-green);
    flex: none;
  }
  .brand-name {
    font-family: "Cinzel", serif;
    font-weight: 400;
    font-size: 34px;
    line-height: 1.15;
    letter-spacing: 1px;
    color: var(--brand-green);
    text-transform: uppercase;
  }
  .person {
    position: absolute;
    left: 70px;
    top: 330px;
    font-family: "Exo 2", sans-serif;
  }
  .person-name {
    font-weight: 600;
    font-size: 40px;
    letter-spacing: 3px;
    color: var(--ink-dark);
    text-transform: uppercase;
  }
  .person-title {
    margin-top: 4px;
    font-weight: 400;
    font-size: 14px;
    letter-spacing: 2px;
    color: var(--ink-mid);
    text-transform: uppercase;
  }
  .contact-panel {
    position: absolute;
    left: 40px;
    top: 455px;
    width: 460px;
    height: 440px;
    border: 2px solid var(--rule-grey);
    border-radius: 36px;
    padding: 20px 30px;
    display: flex;
    flex-direction: column;
  }
  .contact-row {
    flex: 1;
    display: flex;
    align-items: center;
    gap: 30px;
    border-bottom: 1.5px solid var(--rule-grey);
    margin-left: 56px;
    padding-left: 0;
    position: relative;
  }
  .contact-row:last-child { border-bottom: none; }
  .contact-icon {
    position: absolute;
    left: -60px;
    width: 26px;
    height: 26px;
    border: 2px solid var(--brand-green);
    display: flex;
    align-items: center;
    justify-content: center;
    font-family: "Exo 2", sans-serif;
    font-weight: 600;
    font-size: 13px;
    color: var(--brand-green);
  }
  .contact-text {
    font-family: "Exo 2", sans-serif;
    font-size: 18px;
    letter-spacing: 1px;
    color: var(--ink-dark);
    line-height: 1.4;
  }
</style>
</head>
<body>
<main class="canvas">
  <section class="card">
    <header class="brand">
      <span class="brand-mark"></span>
      <div class="brand-name">Maple<br>Lantern<br>Consulting</div>
    </header>

    <div class="person">
      <h1 class="person-name">Daniel Reyes</h1>
      <p class="person-title">General Manager</p>
    </div>

    <div class="contact-panel">
      <div class="contact-row">
        <span class="contact-icon">P</span>
        <span class="contact-text">021 480 3917</span>
      </div>
      <div class="contact-row">
        <span class="contact-icon">E</span>
        <span class="contact-text">hello@maplelantern.com</span>
      </div>
      <div class="contact-row">
        <span class="contact-icon">W</span>
        <span class="contact-text">www.maplelantern.com</span>
      </div>
      <div class="contact-row">
        <span class="contact-icon">A</span>
        <span class="contact-text">42 Orchard Lane,<br>2nd Floor Suite 5</span>
      </div>
    </div>
  </section>
</main>
</body>
</html>
```